Business Card Design

We need business cards designed incorporating our graphics/logo already used on our trucks. We are a small construction company that does everything from building new homes, additions, Kitchens, Baths, Decks, Hardwood Floors/Tile, all phases of construction. No job is too small. We pride ourselves on True Craftmanship/Customer Satisfaction, its what truly separates us from everyone else.

Industry/Entity Type

Construction

Contact Information for Business Card

Maple Ridge Renovations Lic#27KP51986400
342 51st Avenue Gull Harbor NJ 08999
(555)731-2948 Email: info@mapleridgeexample.com
Paul Vandermolen

```html
<!DOCTYPE html>
<html lang="en">
<head>
<meta charset="utf-8">
<title>Maple Ridge Renovations – Business Card</title>
<link rel="stylesheet" href="https://fonts.googleapis.com/css2?family=Baskervville&family=Cinzel:wght@600&display=swap">
<style>
  :root {
    --card-bg: #db5b60;
    --ink: #111111;
    --white: #ffffff;
    --accent-blue: #9fd3e6;
    --name-teal: #3f7f98;
    --name-shadow: #2a4d5c;
    --sky: #a9dcef;
    --sand: #d9a45f;
    --frame: #111111;
  }
  html, body {
    margin: 0;
    padding: 0;
    width: 1200px;
    height: 702px;
    overflow: hidden;
    background: var(--card-bg);
  }
  .card {
    position: relative;
    width: 1200px;
    height: 702px;
    background: var(--card-bg);
    font-family: "Baskervville", "Baskerville", serif;
    color: var(--ink);
  }
  .brand-panel {
    position: absolute;
    left: 46px;
    top: 46px;
    width: 482px;
    height: 206px;
    box-sizing: border-box;
    border: 3px solid var(--frame);
    background: linear-gradient(180deg, var(--sky) 0%, var(--sky) 62%, var(--sand) 72%, var(--sand) 100%);
  }
  .brand-name {
    position: absolute;
    left: 0;
    right: 0;
    top: 76px;
    margin: 0;
    text-align: center;
    font-family: "Baskervville", "Baskerville", serif;
    font-size: 30px;
    font-weight: 400;
    color: var(--ink);
  }
  .holder-name {
    position: absolute;
    left: 607px;
    top: 292px;
    margin: 0;
    font-family: "Cinzel", "Times New Roman", serif;
    font-weight: 600;
    font-size: 45px;
    letter-spacing: 1px;
    color: var(--name-teal);
    text-shadow: 2px 2px 0 var(--name-shadow);
    white-space: nowrap;
    line-height: 1.2;
  }
  .contact-line {
    position: absolute;
    margin: 0;
    font-size: 32px;
    line-height: 1.2;
    white-space: nowrap;
  }
  .contact-address { left: 83px; top: 467px; }
  .contact-phone { left: 229px; top: 512px; }
  .contact-email { left: 119px; top: 557px; }
  .contact-label { color: var(--white); }
  .contact-colon { color: var(--accent-blue); }
  .licence {
    position: absolute;
    left: 637px;
    top: 620px;
    margin: 0;
    font-size: 23px;
    line-height: 1.2;
    white-space: nowrap;
  }
</style>
</head>
<body>
  <div class="card">
    <div class="brand-panel" role="img" aria-label="Company truck graphic: beach scene with biplane banner, two builder characters and service list">
      <p class="brand-name">Maple Ridge Renovations</p>
    </div>

    <h1 class="holder-name">Paul Vandermolen</h1>

    <p class="contact-line contact-address">342 51st Avenue Gull Harbor NJ 08999</p>
    <p class="contact-line contact-phone"><span class="contact-label">TEL</span>:(555)731-2948</p>
    <p class="contact-line contact-email"><span class="contact-label">Email</span><span class="contact-colon">:</span> info@mapleridgeexample.com</p>

    <p class="licence">Maple Ridge Renovations Lic#27KP51986400</p>
  </div>
</body>
</html>
```